Tovane and Partners Business Card

A business card that can be templates for all employees using our newly created logo and information. We are looking for stylish however simplistic in nature, clean looks are better than over the top, however creativity will be appreciated if it has the right appeal. Note: If you feel a type of card (plastic, metalic, carbon, raised lettering, etc) helps your design please specify.
Target Market(s)
Investigation ETC
Industry/Entity Type
Private Investigator
Contact Information for Business Card
Dan Moskel
President
5173 Wexmoor Lane
Hermitage PA 16203-4419
Cell: 724-555-0193; Office: 724-555-0147
Email: danmoskel@tovanepartners-example.com
Requirements
Must have
- Website TovanePartners-example.com
- Name, address, phone number ETC
- Use of current Logo and color pallets if applicable
- TM By logo, small

Nice to have
- Would like to see with and without a photo on the design

Should not have
- Redesign of logo, changing of colors

```html
<!DOCTYPE html>
<html lang="en">
<head>
<meta charset="utf-8">
<title>Tovane and Partners Business Card</title>
<link href="https://fonts.googleapis.com/css2?family=Open+Sans:wght@400;600;700&display=swap" rel="stylesheet">
<style>
  :root {
    --stage: #1f1f1f;
    --card: #000000;
    --accent: #e8431f;
    --ink: #ffffff;
  }
  html, body {
    margin: 0;
    padding: 0;
    width: 1200px;
    height: 800px;
    overflow: hidden;
    background: var(--stage);
    font-family: "Open Sans", Arial, sans-serif;
  }
  .canvas {
    position: relative;
    width: 1200px;
    height: 800px;
  }
  .card {
    position: absolute;
    top: 283px;
    width: 429px;
    height: 239px;
    background: var(--card);
    overflow: hidden;
  }
  .card--front { left: 110px; }
  .card--back { left: 638px; }

  .holder { position: absolute; left: 27px; top: 26px; }
  .holder__name {
    margin: 0;
    color: var(--accent);
    font-size: 14.5px;
    font-weight: 600;
    line-height: 1.1;
  }
  .holder__title {
    margin: 1px 0 0;
    color: var(--ink);
    font-size: 11.5px;
    font-weight: 600;
  }
  .address {
    position: absolute;
    left: 28px;
    top: 104px;
    margin: 0;
    color: var(--ink);
    font-size: 10px;
    line-height: 12.5px;
    font-style: normal;
  }
  .contacts {
    position: absolute;
    left: 28px;
    top: 156px;
    margin: 0;
    padding: 0;
    list-style: none;
    color: var(--ink);
    font-size: 10px;
    line-height: 12.3px;
  }
  .contacts li { display: flex; align-items: center; gap: 4px; }
  .contacts svg { width: 9px; height: 9px; flex: none; }

  .brand {
    position: absolute;
    display: flex;
    align-items: center;
    color: var(--accent);
    font-weight: 700;
    white-space: nowrap;
  }
  .brand__dot {
    border-radius: 50%;
    background: var(--accent);
    flex: none;
  }
  .card--front .brand { left: 212px; top: 156px; font-size: 16px; gap: 7px; }
  .card--front .brand__dot { width: 22px; height: 22px; }
  .card--back .brand { left: 0; right: 0; top: 96px; justify-content: center; font-size: 30px; gap: 14px; }
  .card--back .brand__dot { width: 42px; height: 42px; }

  .accent-band {
    position: absolute;
    left: 0;
    right: 0;
    bottom: 0;
    height: 14px;
    background: var(--accent);
  }
</style>
</head>
<body>
<main class="canvas">
  <section class="card card--front" aria-label="Card front">
    <div class="holder">
      <p class="holder__name">Dan Moskel</p>
      <p class="holder__title">President</p>
    </div>
    <address class="address">5173 Wexmoor Lane<br>Hermitage, PA 16203-4419</address>
    <ul class="contacts">
      <li>
        <svg viewBox="0 0 10 10"><path fill="var(--accent)" d="M2 0.5 L3.6 2.6 L2.8 3.6 C3.4 5 5 6.6 6.4 7.2 L7.4 6.4 L9.5 8 L8.4 9.5 C4.5 9.2 0.8 5.5 0.5 1.6 Z"/></svg>
        (724) 555-0193
      </li>
      <li>
        <svg viewBox="0 0 10 10"><rect x="2.5" y="0.5" width="5" height="9" rx="1" fill="none" stroke="var(--accent)" stroke-width="1.2"/><circle cx="5" cy="8" r="0.6" fill="var(--accent)"/></svg>
        (724) 555-0147
      </li>
      <li>
        <svg viewBox="0 0 10 10"><rect x="0.5" y="2" width="9" height="6.5" fill="var(--accent)"/><path d="M0.8 2.3 L5 5.6 L9.2 2.3" fill="none" stroke="#000" stroke-width="0.8"/></svg>
        danmoskel@tovanepartners-example.com
      </li>
      <li>
        <svg viewBox="0 0 10 10"><circle cx="5" cy="5" r="4.5" fill="var(--accent)"/><path d="M3 2.5 C4.5 3 4 4.5 5.5 5 C6.5 5.5 6 7 5 8" fill="none" stroke="#000" stroke-width="0.9"/></svg>
        www.tovanepartners-example.com
      </li>
    </ul>
    <div class="brand"><span class="brand__dot"></span>Tovane and Partners</div>
    <div class="accent-band"></div>
  </section>

  <section class="card card--back" aria-label="Card back">
    <div class="brand"><span class="brand__dot"></span>Tovane and Partners</div>
  </section>
</main>
</body>
</html>
```